hotel's Website

Hotels website redesign for reference pictures, logo etc see http://restwellmarlow.co.uk/

1. 2-3 Special offers on the main page.
2. Booking calender
3. Location Map
4. Picture gallery.
5. Journeyscope reviews.
6. short description
7. Social Media sharing.
8 Phone number and address.

Industry/Entity Type

Hotel

Requirements
Must have
• 1. 2-3 Special offers on the main page.
2. Booking calender
3. Location Map
4. Picture gallery.
5. Journeyscope reviews.
6. short description
7. Social Media sharing.

```html
<!DOCTYPE html>
<html lang="en">
<head>
<meta charset="utf-8">
<title>Restwell Inn – London Victoria</title>
<link rel="stylesheet" href="https://fonts.googleapis.com/css2?family=Exo+2:wght@300;400&family=Open+Sans:wght@400;600&display=swap">
<style>
  :root {
    --brand-blue: #0a68b9;
    --nav-black: #000;
    --accent-blue: #3a9ee8;
    --ink: #222;
    --ink-soft: #333;
    --panel-grey: #e3e3e3;
    --card-head-top: #dcdcdc;
    --card-head-bottom: #e9e9e9;
    --thumb-grey: #e0e0e0;
    --footer-black: #050505;
    --footer-rule: #1c1c1c;
    --footer-head: #a3a3a3;
    --footer-link: #8c8c8c;
    --white: #fff;
    --display: "Exo 2", "Trebuchet MS", sans-serif;
    --body: "Open Sans", Verdana, sans-serif;
  }
  * { box-sizing: border-box; margin: 0; padding: 0; }
  html, body { width: 715px; height: 1200px; overflow: hidden; background: var(--white); }
  .page { position: relative; width: 715px; height: 1200px; overflow: hidden; font-family: var(--body); color: var(--ink); }

  /* Header */
  .site-header { position: absolute; left: 0; top: 0; width: 715px; height: 111px; background: var(--brand-blue); text-align: center; color: var(--white); }
  .brand { position: absolute; top: 40px; left: 0; width: 100%; display: flex; justify-content: center; align-items: center; gap: 5px; font-family: var(--display); font-weight: 400; font-size: 13px; }
  .brand-dot { width: 9px; height: 9px; border-radius: 50%; background: var(--white); }
  .brand-location { position: absolute; top: 76px; width: 100%; font-family: var(--display); font-weight: 300; font-size: 12px; color: #d4e6f7; }

  /* Navigation */
  .main-nav { position: absolute; left: 25px; top: 111px; width: 665px; height: 33px; background: var(--nav-black); display: flex; justify-content: center; align-items: center; gap: 17px; }
  .main-nav a { font-family: var(--display); font-weight: 400; font-size: 9.5px; color: var(--white); text-decoration: none; letter-spacing: 0.2px; }
  .main-nav a.is-current { color: var(--accent-blue); }

  /* Hero */
  .hero { position: absolute; left: 25px; top: 144px; width: 665px; height: 306px; background: linear-gradient(180deg, #56706f 0%, #3c4a52 45%, #2b2a33 75%, #1a1b22 100%); }
  .booking { position: absolute; left: 499px; top: 35px; width: 150px; height: 135px; background: rgba(120,128,140,0.55); }
  .booking h2 { position: absolute; left: 10px; top: 11px; font-family: var(--display); font-weight: 300; font-size: 18.5px; color: #1c2230; letter-spacing: 0.5px; }
  .date-field { position: absolute; left: 10px; width: 131px; height: 15px; background: var(--white); font-size: 7px; color: #777; padding: 2px 7px; }
  .date-field::after { content: ""; position: absolute; right: 7px; top: 5px; border-left: 4px solid transparent; border-right: 4px solid transparent; border-top: 4px solid #111; }
  .date-field.arrive { top: 47px; }
  .date-field.depart { top: 77px; }
  .booking-search { position: absolute; left: 69px; top: 107px; }

  /* Welcome */
  .welcome { position: absolute; left: 52px; top: 466px; width: 443px; }
  .section-title { font-family: var(--display); font-weight: 300; font-size: 19px; color: var(--ink); }
  .welcome p { margin-top: 14px; font-size: 8.4px; line-height: 11.6px; text-align: justify; color: var(--ink); }
  .welcome p + p { margin-top: 12px; }
  .read-more { font-family: var(--display); font-weight: 400; font-size: 9px; color: var(--ink); text-decoration: none; }
  .welcome .read-more { position: absolute; right: 0; top: 171px; }

  /* Reviews */
  .reviews { position: absolute; left: 529px; top: 466px; width: 160px; }
  .review { position: absolute; left: 0; width: 160px; height: 34px; }
  .review-thumb { position: absolute; left: 0; top: 0; width: 34px; height: 34px; background: var(--thumb-grey); }
  .review-name { position: absolute; left: 38px; top: 0; font-size: 7.4px; color: var(--ink); }
  .review-text { position: absolute; left: 38px; top: 10px; width: 122px; font-size: 6.5px; line-height: 9px; color: var(--ink); }

  /* Feature cards */
  .card { position: absolute; top: 681px; width: 196px; height: 314px; background: var(--panel-grey); }
  .card-head { height: 42px; background: linear-gradient(180deg, var(--card-head-top), var(--card-head-bottom)); display: flex; align-items: center; justify-content: center; font-family: var(--display); font-weight: 300; font-size: 14.5px; color: var(--ink-soft); letter-spacing: 0.4px; }
  .card-photo { height: 129px; }
  .card-body { padding: 17px 18px 0; font-size: 8.4px; line-height: 11.8px; text-align: justify; color: var(--ink); }
  .card .read-more { position: absolute; right: 17px; top: 286px; }
  .card.offers { left: 25px; }
  .card.explore { left: 259px; }
  .card.stay { left: 494px; }
  .offers .card-photo { background: linear-gradient(160deg, #2d4e9a 0%, #3b63b6 40%, #b9873a 75%, #6e3b17 100%); }
  .explore .card-photo { background: linear-gradient(180deg, #4e4b73 0%, #8a6a6c 45%, #a66fb8 70%, #2a2236 100%); }
  .stay .card-photo { background: linear-gradient(180deg, #cbbd97 0%, #d8c28c 45%, #f1ece4 70%, #8e2b22 100%); }

  /* Footer */
  .site-footer { position: absolute; left: 0; top: 1038px; width: 715px; height: 162px; background: var(--footer-black); }
  .footer-col { position: absolute; top: 0; height: 162px; padding-top: 33px; }
  .footer-col + .footer-col { border-left: 1px solid var(--footer-rule); }
  .footer-col h3 { font-size: 9.4px; font-weight: 600; color: var(--footer-head); margin-bottom: 4px; }
  .footer-col a { display: block; font-size: 9.2px; line-height: 17.4px; color: var(--footer-link); text-decoration: none; }
</style>
</head>
<body>
<div class="page">

  <header class="site-header">
    <div class="brand"><span class="brand-dot"></span>Restwell Inn</div>
    <div class="brand-location">London | Victoria</div>
  </header>

  <nav class="main-nav">
    <a class="is-current" href="#">HOME</a>
    <a href="#">OUR ROOM</a>
    <a href="#">ATTRACTIONS</a>
    <a href="#">SPECIAL OFFERS</a>
    <a href="#">GALLERY</a>
    <a href="#">DIRECTIONS</a>
    <a href="#">CONTACT</a>
  </nav>

  <section class="hero" role="img" aria-label="Night view of the London skyline with a lit bascule bridge over the Thames">
    <form class="booking">
      <h2>BOOK A ROOM</h2>
      <div class="date-field arrive">November 17, 2013</div>
      <div class="date-field depart">November 25, 2013</div>
      <svg class="booking-search" width="12" height="12" viewBox="0 0 12 12" aria-label="Search">
        <circle cx="4.5" cy="4.5" r="3.3" fill="none" stroke="#111" stroke-width="1.6"/>
        <line x1="7" y1="7" x2="11" y2="11" stroke="#111" stroke-width="2"/>
      </svg>
    </form>
  </section>

  <section class="welcome">
    <h1 class="section-title">Welcome to London Victoria</h1>
    <p>Lorem ipsum dolor sit amet, consectetur adipiscing elit. Fusce a cursus justo. Aenean at mi semper, eleifend magna vel, tempor quam. Maecenas viverra fermentum laoreet. Aliquam rutrum vel diam vitae laoreet. Nulla a tellus et urna vehicula ornare. Fusce aliquam diamor erat aliquam. Donec ligula libero, sodales non mollis ac, dictum at sapien. Lorem ipsum dolor sit amet, consectetu</p>
    <p>Lorem ipsum dolor sit amet, consectetur adipiscing elit. Fusce a cursus justo. Aenean at mi semper, eleifend magna vel, tempor quam. Maecenas viverra fermentum laoreet. Aliquam rutrum vel diam vitae laoreet. Nulla a tellus et urna vehicula ornare. Fusce aliquam diamor erat aliquam. Donec ligula libero, sodales non mollis ac, dictum at sapien.r adipiscing elit. Fusce a cursus justo. Aenean at ma ornare. Fusce aliquam diamor erat aliquam. Donec ligula libero, sodales non mollis ac, dictum at sapien.</p>
    <a class="read-more" href="#">+ Read More</a>
  </section>

  <aside class="reviews">
    <h2 class="section-title">Client reviews</h2>
    <div class="review" style="top:39px">
      <div class="review-thumb"></div>
      <div class="review-name">Peter Hollis</div>
      <div class="review-text">Lorem ipsum dolor sit amet, consec tur adipiscing elit.</div>
    </div>
    <div class="review" style="top:96px">
      <div class="review-thumb"></div>
      <div class="review-name">Clara M.</div>
      <div class="review-text">Lorem ipsum dolor sit amet, consec tur adipiscing elit.</div>
    </div>
    <div class="review" style="top:151px">
      <div class="review-thumb"></div>
      <div class="review-name">Rosa</div>
      <div class="review-text">Lorem ipsum dolor sit amet, consec tur adipiscing elit.</div>
    </div>
  </aside>

  <article class="card offers">
    <h2 class="card-head">SPECIAL OFFERS</h2>
    <div class="card-photo" role="img" aria-label="Parliament clock tower at dusk with light trails"></div>
    <p class="card-body">Lorem ipsum dolor sit amet, consecte-tur adipiscing elit. Fusce a cursus justo. Aenean at mi semper, eleifend magna vel, tempor quam. Maecenas viverra fermentum laoreet. Aliquam rutrum vel diam vitae laoreet. Nulla a tellus et urna vehicula ornare. Fligula libero, sodales non molli</p>
    <a class="read-more" href="#">+ Read More</a>
  </article>

  <article class="card explore">
    <h2 class="card-head">EXPLORE LONDON</h2>
    <div class="card-photo" role="img" aria-label="Observation wheel lit purple beside the river at twilight"></div>
    <p class="card-body">Lorem ipsum dolor sit amet, consecte-tur adipiscing elit. Fusce a cursus justo. Aenean at mi semper, eleifend magna vel, tempor quam. Maecenas viverra fermentum laoreet. Aliquam rutrum vel diam vitae laoreet. Nulla a tellus et urna vehicula ornare. Fligula libero, sodales non molli</p>
    <a class="read-more" href="#">+ Read More</a>
  </article>

  <article class="card stay">
    <h2 class="card-head">STAY IN COMFORT</h2>
    <div class="card-photo" role="img" aria-label="Hotel bedroom with a made double bed and red cushions"></div>
    <p class="card-body">Lorem ipsum dolor sit amet, consecte-tur adipiscing elit. Fusce a cursus justo. Aenean at mi semper, eleifend magna vel, tempor quam. Maecenas viverra fermentum laoreet. Aliquam rutrum vel diam vitae laoreet. Nulla a tellus et urna vehicula ornare. Fligula libero, sodales non molli</p>
    <a class="read-more" href="#">+ Read More</a>
  </article>

  <footer class="site-footer">
    <div class="footer-col" style="left:0;width:141px;padding-left:42px">
      <h3>Useful links</h3>
      <a href="#">dolor sit amet</a><a href="#">sit ut duis</a><a href="#">molestie</a><a href="#">augue homero</a>
    </div>
    <div class="footer-col" style="left:141px;width:140px;padding-left:41px">
      <h3>Cruise Info</h3>
      <a href="#">dolor sit amet</a><a href="#">sit ut duis</a><a href="#">molestie</a><a href="#">augue homero</a>
    </div>
    <div class="footer-col" style="left:281px;width:140px;padding-left:31px">
      <h3>About Harbourline</h3>
      <a href="#">dolor sit amet</a><a href="#">sit ut duis</a><a href="#">molestie</a><a href="#">augue homero</a>
    </div>
    <div class="footer-col" style="left:421px;width:143px;padding-left:41px">
      <h3>Shipping</h3>
      <a href="#">dolor sit amet</a><a href="#">sit ut duis</a><a href="#">molestie</a><a href="#">augue homero</a>
    </div>
    <div class="footer-col" style="left:564px;width:151px;padding-left:40px">
      <h3>Follow us on</h3>
      <a href="#">Circlepage</a><a href="#">Chirpline</a><a href="#">Workmesh</a><a href="#">Orbit Plus</a>
    </div>
  </footer>

</div>
</body>
</html>
```